Curry Sauce label design

Old family recipe for curry sauce passed down thru generations. My Dad, Tobin passed the recipe to me and the family now wants to market the sauce. My father has passed away and we want the sauce to be named after him and the label on the jars to have his picture. Sauce name (for now) is "Tobin's Curry Sauce"

We need a label for the sauce jar. We like the styles of "Garrick Hearth", "Lo Vee Bimma" and "Plucked at Dawn" labels. Use those as style references. I have attached images of those labels and also attached my fathers photo. Note that we want the photo styalized like they did with Garrick Hearth or other styalization i.e. many photo effects software out there (free) that can turn a photo to line drawing, pastel, oil painting look etc...

the label will need a back label space provided with fonts we can use so we can add the ingredients and nutrition info and other info that you typically see on back of jar. We need label to be able to be upsized or down sized and not lose any resolution or clarity so we can apply to both a 12oz and a 16oz jar

I will be extending the timeline for this project

Need extra days to review

Industry/Entity Type

Food/sauces/curry sauce

Colors
FFC000
F8CF3A
FAE287
FDF2CF
FEFAEE

Requirements
Must have
• Fathers name and image in label

```html
<!DOCTYPE html>
<html lang="en">
<head>
<meta charset="utf-8">
<title>Tobin's Curry Sauce – Jar Label</title>
<link rel="stylesheet" href="https://fonts.googleapis.com/css2?family=Federo&family=Marcellus+SC&family=Kaushan+Script&display=swap">
<style>
  :root {
    --page-bg: #ffffff;
    --band-red: #c4262c;
    --pattern-orange: #f0662c;
    --pattern-amber: #f7a43a;
    --arch-red: #e0442c;
    --arch-deep: #d2362a;
    --ribbon-red: #b21f2a;
    --ribbon-dark: #7e1219;
    --ribbon-edge: #d8484f;
    --stripe-pink: #e55aa4;
    --band-lilac: #b98ac8;
    --band-purple: #6b1f7c;
    --title-white: #ffffff;
    --script-lilac: #f6e6fb;
    --portrait-cream: #fdf2cf;
    --portrait-warm: #f8cf3a;
  }
  * { box-sizing: border-box; }
  html, body {
    margin: 0;
    width: 1200px;
    height: 1200px;
    overflow: hidden;
    background: var(--page-bg);
  }
  .canvas {
    position: relative;
    width: 1200px;
    height: 1200px;
  }
  .label {
    position: absolute;
    left: 50px;
    top: 320px;
    width: 1100px;
    height: 560px;
  }
  .brand-title {
    font-family: "Federo", "Marcellus SC", sans-serif;
    font-size: 128px;
    fill: var(--title-white);
    letter-spacing: 2px;
  }
  .product-name {
    font-family: "Marcellus SC", serif;
    font-size: 54px;
    fill: var(--title-white);
    stroke: #3a0a0e;
    stroke-width: 3px;
    paint-order: stroke;
  }
  .tagline {
    font-family: "Kaushan Script", cursive;
    font-size: 44px;
    fill: var(--script-lilac);
  }
</style>
</head>
<body>
<main class="canvas">
  <svg class="label" viewBox="0 0 1100 560" xmlns="http://www.w3.org/2000/svg">
    <defs>
      <linearGradient id="pattern-fill" x1="0" y1="0" x2="1" y2="0">
        <stop offset="0" stop-color="var(--pattern-orange)"/>
        <stop offset="0.5" stop-color="var(--pattern-amber)"/>
        <stop offset="1" stop-color="var(--pattern-orange)"/>
      </linearGradient>
      <linearGradient id="arch-fill" x1="0" y1="0" x2="0" y2="1">
        <stop offset="0" stop-color="var(--arch-deep)"/>
        <stop offset="1" stop-color="var(--arch-red)"/>
      </linearGradient>
      <linearGradient id="purple-fill" x1="0" y1="0" x2="1" y2="0">
        <stop offset="0" stop-color="var(--band-lilac)"/>
        <stop offset="0.45" stop-color="var(--band-purple)"/>
        <stop offset="1" stop-color="var(--band-purple)"/>
      </linearGradient>
      <linearGradient id="portrait-fill" x1="0" y1="0" x2="0" y2="1">
        <stop offset="0" stop-color="var(--arch-red)"/>
        <stop offset="0.35" stop-color="var(--portrait-cream)"/>
        <stop offset="1" stop-color="var(--portrait-warm)"/>
      </linearGradient>
    </defs>

    <!-- top band and patterned field -->
    <rect class="top-band" x="0" y="0" width="1100" height="50" fill="var(--band-red)"/>
    <rect class="pattern-field" x="0" y="40" width="1100" height="370" fill="url(#pattern-fill)"
          role="img" aria-label="Ornamental lattice pattern in orange and gold"/>

    <!-- arch frame -->
    <path class="arch" d="M335 410 V230 A215 215 0 0 1 765 230 V410 Z" fill="url(#arch-fill)"/>
    <text class="brand-title" x="550" y="180" text-anchor="middle">TOBIN'S</text>

    <!-- portrait area -->
    <rect class="portrait" x="420" y="195" width="260" height="215" fill="url(#portrait-fill)"
          role="img" aria-label="Stylised painted portrait of Tobin seated in a white shirt"/>

    <!-- lower bands -->
    <rect class="stripe-pink" x="0" y="400" width="1100" height="34" fill="var(--stripe-pink)"/>
    <rect class="band-purple" x="0" y="430" width="1100" height="130" fill="url(#purple-fill)"/>

    <!-- ribbon -->
    <path class="ribbon-tail" d="M300 378 L420 370 L420 420 L318 426 L340 400 Z" fill="var(--ribbon-dark)"/>
    <path class="ribbon-tail" d="M800 378 L680 370 L680 420 L782 426 L760 400 Z" fill="var(--ribbon-dark)"/>
    <rect class="ribbon" x="352" y="392" width="396" height="80" fill="var(--ribbon-red)"
          stroke="var(--ribbon-edge)" stroke-width="3"/>
    <text class="product-name" x="550" y="450" text-anchor="middle">CURRY SAUCE</text>

    <text class="tagline" x="550" y="525" text-anchor="middle">Family Recipe</text>
  </svg>
</main>
</body>
</html>
```